Stationary for Harbour Crest

we are in the process of creating a more professional image for our company Harbour Crest Paramedical Services. We have recently had a new logo and general brochure designed using pitchforge and have been impressed by the quality of submissions.

We need:
- Letterhead (A4)
- Business Cards
- With compliments slips
- Email stationary

Letterhead information:
Address - 47 Wendock Street, Kelmont Vic 3094
Phone - 1800 426 318
email - enquiries@harbourcrestmed.com.au
Internet - www.harbourcrestmed.com.au
ABN - 31 862 507 194
ACN - 274 618 053

Files need to be able to be edited in Illustrator CS2

Business Cards / with compliments slips / email stationary:
Double sided.
One side to have Name, Mobile number, company phone 1800426318, email, internet address

Files need to be able to be edited in Illustrator CS2 (except email stationary)

Our website is www.harbourcrestmed.com.au for more information. Do not base designs on the website as it will eventually be revised.

Target Market(s)

Australian based businesses, government departments and schools. We specialise in corporate customers rather than public first aid course

Requirements
Must have
• Where applicable file to be editable in illustrator CS2 to allow future alterations.

```html
<!DOCTYPE html>
<html lang="en">
<head>
<meta charset="utf-8">
<title>Harbour Crest – With Compliments Slip</title>
<link rel="stylesheet" href="https://fonts.googleapis.com/css2?family=Nunito+Sans:wght@400;600;700;800&display=swap">
<style>
  :root {
    --canvas: #ffffff;
    --slip-paper: #f4f3ee;
    --brand-red: #e2434b;
    --brand-grey: #58585a;
    --ink: #111111;
    --rule: #555555;
  }
  * { box-sizing: border-box; margin: 0; padding: 0; }
  html, body {
    width: 1200px; height: 800px; overflow: hidden;
    background: var(--canvas);
    font-family: "Nunito Sans", Arial, sans-serif;
    color: var(--ink);
  }
  .stage { position: relative; width: 1200px; height: 800px; }

  .slip {
    position: absolute; left: 190px;
    width: 820px; height: 373px;
    border: 1px solid #dddbd4;
  }
  .slip--front { top: 20px; background: var(--slip-paper); }
  .slip--back  { top: 407px; background: #fff; }

  .slip__pattern {
    position: absolute; inset: 0;
    background: linear-gradient(135deg,
      var(--brand-grey) 0%, var(--brand-red) 30%,
      var(--brand-grey) 55%, var(--brand-red) 80%, var(--brand-grey) 100%);
  }

  .brand {
    position: absolute; left: 26px; top: 205px;
    display: flex; align-items: center; gap: 10px;
    color: var(--brand-red); font-weight: 800;
  }
  .brand__mark { width: 40px; height: 40px; background: var(--brand-red); }
  .brand__name { font-size: 24px; line-height: 1; letter-spacing: -0.2px; }
  .brand__sub { display: block; font-size: 11px; line-height: 1.3; margin-top: 3px; }

  .note {
    position: absolute; left: 290px; top: 26px; width: 502px;
  }
  .note__title {
    font-size: 23px; font-weight: 700; letter-spacing: -0.3px;
    line-height: 1; height: 32px;
  }
  .note__lines { list-style: none; }
  .note__lines li {
    height: 28.8px; border-top: 1px dotted var(--rule);
  }

  .contact {
    position: absolute; left: 290px; top: 317px;
    font-size: 11.2px; line-height: 14px; white-space: nowrap;
    font-style: normal;
  }
  .contact b { font-weight: 800; }
</style>
</head>
<body>
<main class="stage">
  <section class="slip slip--front">
    <div class="brand">
      <span class="brand__mark" aria-hidden="true"></span>
      <p class="brand__name">Harbour Crest<span class="brand__sub">Paramedical Services Pty Ltd</span></p>
    </div>

    <div class="note">
      <h1 class="note__title">With Compliments</h1>
      <ul class="note__lines">
        <li></li><li></li><li></li><li></li><li></li><li></li><li></li><li></li>
      </ul>
    </div>

    <address class="contact">
      <b>47 Wendock Street Kelmont VIC 3094</b><br>
      <b>Phone</b> 1800 426 318 <b>Email</b> enquiries@harbourcrestmed.com.au <b>Web</b> www.harbourcrestmed.com.au
    </address>
  </section>

  <section class="slip slip--back">
    <div class="slip__pattern" role="img" aria-label="Reverse side: repeating red and charcoal brand pattern"></div>
  </section>
</main>
</body>
</html>
```